Design/Build Engineering and Detailing Service 3D Modeling

We are an engineering company in the construction industry. We specialize in designing blueprints for new construction projects such as high rise buildings, hospitals, hotels, public schools, large scale apartment buildings etc.

We want to have a clean, modern, cutting edge design, but it should be clear and easy to navigate. Related videos in the background of the page are a plus. For example The page now has a picture of the marlow crest span in san francisco with fog rolling over it and cars driving on the bridge, saying website coming soon. This is played at a faster frame rate. We want to have customer portal to access files, fill out work orders, pay invoices, make suggestions etc.
Updates

Target Market(s)

Los Angeles, San francisco, San Jose, Portland, Seattle, Las Vegas, Denver

Industry/Entity Type

Construction

Coding

Coded - Design and coding required

Number of Pages Required

4 page

Font styles to use
Serif
Sans Serif

Colors
3276b5
0255a3
85acd3
9d9d9d
5c5c5c
ec1f27
000000
fbee3f
00a990

Requirements
Must have
• Work Examples, mission statement, team members, capabilities. Convey the technical aspects of the business in a way that someone can understand the companies capabilities without knowing the technical side of the business.
Nice to have
• Construction related Videos, Downtown city center skylines, clean, modern, concise design.
Should not have
• Overly complex navigation. should not be to busy

```html
<!DOCTYPE html>
<html lang="en">
<head>
<meta charset="utf-8">
<title>Norvale Design Inc.</title>
<link href="https://fonts.googleapis.com/css2?family=Lato:wght@400;700;900&family=Raleway:wght@300;400;600;700&display=swap" rel="stylesheet">
<style>
:root{
  --blue:#3276b5;
  --blue-deep:#0255a3;
  --blue-light:#85acd3;
  --cyan:#1a9ad6;
  --grey:#9d9d9d;
  --grey-dark:#5c5c5c;
  --ink:#222;
  --topbar:#2b2b2b;
  --footer:#2e2e2e;
  --footer-base:#1f1f1f;
  --band:#e9e9e9;
  --white:#fff;
}
*{margin:0;padding:0;box-sizing:border-box}
html,body{width:1200px;height:3291px;overflow:hidden}
body{font-family:"Lato",sans-serif;color:var(--ink);background:var(--white);position:relative}
.abs{position:absolute}
section,header,footer,.topbar{position:absolute;left:0;width:1200px}

/* top bar */
.topbar{top:0;height:40px;background:var(--topbar);color:#ddd;font-size:14px}
.topbar .contact{left:110px;top:0;height:40px;display:flex;align-items:center;gap:34px}
.topbar .contact span{display:flex;align-items:center;gap:8px}
.topbar .licence{left:590px;top:5px;font-size:11px;font-weight:700;color:#fff;line-height:14px;text-align:right;width:120px}
.topbar .btn{top:0;height:40px;display:flex;align-items:center;gap:10px;color:#fff;font-weight:900;font-size:14px;padding-left:14px}
.btn-quote{left:724px;width:190px;background:var(--blue)}
.btn-pay{left:914px;width:188px;background:var(--blue-deep)}

/* header */
header{top:40px;height:103px;background:var(--white)}
.brand{left:100px;top:18px;display:flex;flex-direction:column;align-items:center;gap:6px}
.brand .mark{width:40px;height:40px;background:var(--blue)}
.brand .name{font-weight:700;font-size:14px;color:var(--blue);letter-spacing:.5px}
.nav{left:494px;top:42px;display:flex;font-size:15px;font-weight:700;color:#333}
.nav a{color:inherit;text-decoration:none;padding:0 16px;border-left:1px solid #999;line-height:16px}
.nav a:first-child{border-left:none;color:var(--blue);border-bottom:2px solid var(--blue)}

/* hero */
.hero{top:143px;height:460px;background:linear-gradient(135deg,#1b2230 0%,#3b4660 35%,#6a3d7a 55%,#1f5a8a 75%,#111 100%)}
.hero .arrow{top:205px}
.hero .caption{left:100px;top:274px;width:1056px;height:110px;background:rgba(40,40,40,.72)}
.hero .avatar{left:0;top:0;width:120px;height:110px;background:linear-gradient(180deg,#1e88c8,#0d5a8c)}
.hero .caption p{position:absolute;left:120px;top:24px;color:#fff;font-family:"Raleway",sans-serif;font-weight:700;font-size:21px;line-height:32px;text-transform:uppercase}
.hero .cta{left:837px;top:33px;width:143px;height:44px;background:var(--cyan);color:#fff;font-weight:700;font-size:14px;display:flex;align-items:center;justify-content:center;text-transform:uppercase}
.hero .dots{left:570px;top:412px;display:flex;gap:6px}
.hero .dots i{display:block;width:18px;height:4px;background:#888}
.hero .dots i.on{background:#fff}

/* shared titles */
.title{width:1200px;left:0;text-align:center;font-family:"Raleway",sans-serif;font-weight:400;font-size:36px;text-transform:uppercase;color:#222}
.title b{font-weight:400;color:var(--blue)}
.divider{left:400px;width:400px;height:20px}

/* welcome */
.welcome{top:603px;height:411px}
.welcome .title{top:50px}
.welcome .lead{left:127px;top:150px;width:948px;font-size:14px;line-height:27px;text-align:center;color:#333}
.mv{top:286px;display:flex;gap:14px;align-items:flex-start}
.mv h3{font-family:"Raleway",sans-serif;font-weight:700;font-size:15px;color:#111;margin:6px 0 3px}
.mv p{font-size:11px;line-height:13px;color:#555;width:170px}

/* services */
.services{top:1014px;height:467px;background:var(--band)}
.services .title{top:40px;text-transform:none;font-size:38px}
.card{top:158px;width:486px;height:241px;background:#fff;border-radius:6px;box-shadow:0 1px 4px rgba(0,0,0,.15);overflow:hidden}
.card .pic{left:0;top:0;width:246px;height:241px}
.card h3{position:absolute;left:262px;top:22px;font-family:"Raleway",sans-serif;font-weight:700;font-size:16px;color:#111}
.card p{position:absolute;left:262px;top:52px;width:210px;font-size:12.5px;line-height:19px;color:#333}
.card .more{left:262px;top:178px;width:103px;height:30px;background:var(--cyan);color:#fff;font-weight:700;font-size:12px;display:flex;align-items:center;justify-content:center}

/* capabilities */
.capabilities{top:1481px;height:548px;background:#fff}
.capabilities .title{top:48px}
.cap-art{left:263px;top:118px;width:680px;height:410px;background:radial-gradient(ellipse at center,#eceef1 0%,#f4f5f7 55%,#fff 80%)}
.cap-core{left:513px;top:257px;width:158px;height:158px;border-radius:50%;background:#fff;box-shadow:0 0 0 6px #eef2f6;display:flex;flex-direction:column;align-items:center;justify-content:center;gap:8px}
.cap-core .mark{width:34px;height:34px;background:var(--blue)}
.cap-core span{font-weight:700;font-size:13px;color:var(--blue)}
.cap{display:flex;align-items:center;gap:24px}
.cap .ico{width:70px;height:70px;display:flex;align-items:center;justify-content:center}
.cap .lbl{font-family:"Raleway",sans-serif;font-weight:700;font-size:15px;line-height:16px;color:#222}
.dot{width:9px;height:9px;border-radius:50%;background:var(--cyan)}

/* projects */
.projects{top:2029px;height:472px;background:linear-gradient(180deg,#3a3f46 0%,#4e545c 40%,#2f3238 100%)}
.projects .title{top:18px;color:#fff}
.projects .divider{top:74px}
.proj{top:141px;width:318px;height:224px;background:#fff}
.proj .pic{left:0;top:0;width:318px;height:171px}
.proj .bar{left:0;top:171px;width:318px;height:53px;background:#fff}
.proj .bar span{position:absolute;left:16px;top:16px;font-family:"Raleway",sans-serif;font-weight:700;font-size:18px;color:#111}
.proj .go{right:0;top:0;width:80px;height:53px;background:var(--cyan);clip-path:polygon(22% 0,100% 0,100% 100%,0 100%);display:flex;align-items:center;justify-content:center;padding-left:14px}
.pager{top:2431px;left:567px;display:flex;gap:8px}
.pager i{width:28px;height:28px;background:#fff;border-radius:3px;display:flex;align-items:center;justify-content:center}

/* videos */
.videos{top:2501px;height:468px;display:grid;grid-template-columns:repeat(3,1fr);grid-template-rows:repeat(2,1fr);gap:2px;background:#111}
.video{position:relative}
.video .play{position:absolute;left:50%;top:50%;width:74px;height:46px;margin:-23px 0 0 -37px;background:rgba(255,255,255,.85);border-radius:8px;display:flex;align-items:center;justify-content:center}

/* footer */
footer{top:2969px;height:278px;background:var(--footer);color:#ccc}
footer h4{position:absolute;top:40px;font-family:"Raleway",sans-serif;font-weight:400;font-size:19px;color:#fff}
footer .rule{position:absolute;top:76px;height:1px;background:#555}
.f-item{display:flex;align-items:flex-start;gap:18px;font-size:12px;line-height:16px;color:#aaa}
.f-item .c{width:26px;height:26px;border-radius:50%;background:#444;flex:none;display:flex;align-items:center;justify-content:center}
.f-item b{color:#ddd;font-weight:700;display:block}
.news p{font-size:12.5px;line-height:18px;color:#ddd;width:150px}
.news form{display:flex;position:absolute;left:0;top:114px}
.news .field{width:155px;height:32px;background:#fff;font-size:11px;color:#444;display:flex;align-items:center;padding-left:26px;border-radius:4px 0 0 4px}
.news .sub{width:92px;height:32px;background:var(--cyan);color:#fff;font-weight:700;font-size:11px;display:flex;align-items:center;justify-content:center;text-transform:uppercase}
.links li{list-style:none;font-size:11.5px;color:#ddd;margin-bottom:16px;display:flex;align-items:center;gap:8px}
.links li::before{content:"";width:4px;height:4px;background:#ccc;border-radius:50%}
.social{display:flex;gap:6px}
.social i{display:block;width:29px;height:29px;background:var(--blue)}
.f-brand{display:flex;flex-direction:column;align-items:center;gap:6px}
.f-brand .mark{width:30px;height:30px;background:#ddd}
.f-brand span{font-weight:700;font-size:12px;color:#ddd}
.copy{position:absolute;left:0;top:3247px;width:1200px;height:44px;background:var(--footer-base);color:#ccc;font-size:12.5px;display:flex;align-items:center;justify-content:center}
</style>
</head>
<body>

<div class="topbar">
  <div class="abs contact">
    <span><svg width="14" height="14" viewBox="0 0 24 24"><path fill="#3a9ad9" d="M6.6 10.8a15 15 0 0 0 6.6 6.6l2.2-2.2c.3-.3.7-.4 1-.2 1.1.4 2.3.6 3.6.6.6 0 1 .4 1 1V20c0 .6-.4 1-1 1A17 17 0 0 1 3 4c0-.6.4-1 1-1h3.5c.6 0 1 .4 1 1 0 1.3.2 2.5.6 3.6.1.3 0 .7-.2 1z"/></svg>555-018-2046</span>
    <span><svg width="16" height="12" viewBox="0 0 16 12"><rect width="16" height="12" rx="1" fill="#3a9ad9"/><path d="M1 1l7 6 7-6" stroke="#2b2b2b" stroke-width="1.4" fill="none"/></svg>info@norvaledesign.com</span>
  </div>
  <div class="abs licence">Licence No: 480153K<br>ABN 61 208 774 305</div>
  <div class="abs btn btn-quote"><svg width="22" height="22" viewBox="0 0 24 24"><path d="M3 17l10-10 4 4-10 10H3z" fill="#fff"/><path d="M15 5l2-2 4 4-2 2z" fill="#fff"/></svg>REQUEST A QUOTE</div>
  <div class="abs btn btn-pay"><svg width="22" height="22" viewBox="0 0 24 24"><circle cx="12" cy="12" r="10" fill="#fff"/><path d="M12 6v12M8 9h6a2 2 0 0 1 0 4h-4a2 2 0 0 0 0 4h6" stroke="#0255a3" stroke-width="2" fill="none"/></svg>MAKE A PAYMENT</div>
</div>

<header>
  <div class="abs brand"><div class="mark"></div><div class="name">NORVALE DESIGN INC.</div></div>
  <nav class="abs nav"><a>Home</a><a>About Us</a><a>Services</a><a>Capabilities</a><a>Projects</a><a>Contact Us</a></nav>
</header>

<section class="hero" role="img" aria-label="Colour-coded 3D model of building piping and ductwork">
  <svg class="abs arrow" style="left:40px" width="30" height="60" viewBox="0 0 30 60"><path d="M26 2L4 30l22 28" stroke="#fff" stroke-width="3" fill="none"/></svg>
  <svg class="abs arrow" style="left:1130px" width="30" height="60" viewBox="0 0 30 60"><path d="M4 2l22 28L4 58" stroke="#fff" stroke-width="3" fill="none"/></svg>
  <div class="abs caption">
    <div class="abs avatar" role="img" aria-label="Engineer in a hard hat illustration"></div>
    <p>We specialize in designing blueprints for new<br>construction projects such as high rise buildings</p>
    <div class="abs cta">Get Started</div>
  </div>
  <div class="abs dots"><i class="on"></i><i></i><i></i></div>
</section>

<section class="welcome">
  <h2 class="abs title">Welcome to <b>Norvale Design Inc</b></h2>
  <svg class="abs divider" style="top:106px" viewBox="0 0 400 20"><line x1="20" y1="10" x2="380" y2="10" stroke="#999"/><rect x="188" y="2" width="24" height="16" fill="#fff"/><rect x="193" y="5" width="14" height="10" fill="none" stroke="#777"/></svg>
  <p class="abs lead">Lorem ipsum dolor sit amet, consectetuer adipiscing elit, sed diam nonummy nibh euismod tincidunt ut laoreet dolore magna aliquam erat volutpat. Ut wisi enim ad minim veniam, quis nostrud exerci tation ullamcorper suscipit lobortis nisl ut aliquip ex ea commodo consequat. Duis autem vel eum iriure dolor in hendrerit in vulputate velit esse molestie consequat, vel illum dolore eu feugiat nulla facilisis at vero eros et accumsan et iusto odio dignissim qui blandit praesent luptatum zzril delenit augue duis dolore te feugait nulla facilisi.</p>
  <div class="abs mv" style="left:336px">
    <svg width="70" height="70" viewBox="0 0 70 70"><circle cx="35" cy="35" r="32" fill="#fff" stroke="var(--blue-deep)" stroke-width="3"/><circle cx="35" cy="27" r="6" fill="var(--blue-deep)"/><circle cx="23" cy="31" r="5" fill="var(--blue-deep)"/><circle cx="47" cy="31" r="5" fill="var(--blue-deep)"/><path d="M25 48a10 10 0 0 1 20 0zM14 48a9 9 0 0 1 12-8M56 48a9 9 0 0 0-12-8" fill="var(--blue-deep)"/></svg>
    <div><h3>OUR MISSION</h3><p>Sed ut perspiciatis unde omnis iste natus error sit voluptatem accusantium.</p></div>
  </div>
  <div class="abs mv" style="left:618px">
    <svg width="70" height="70" viewBox="0 0 70 70"><circle cx="35" cy="35" r="32" fill="#fff" stroke="var(--blue-deep)" stroke-width="3"/><circle cx="35" cy="35" r="18" fill="none" stroke="var(--blue-deep)" stroke-width="4"/><circle cx="35" cy="35" r="9" fill="none" stroke="var(--blue-deep)" stroke-width="4"/><path d="M35 35L52 18M47 18h5v5" stroke="var(--blue-deep)" stroke-width="3" fill="none"/></svg>
    <div><h3>OUR VISION</h3><p>Sed ut perspiciatis unde omnis iste natus error sit voluptatem accusantium.</p></div>
  </div>
</section>

<section class="services">
  <h2 class="abs title">Our <b>Services</b></h2>
  <svg class="abs divider" style="top:100px" viewBox="0 0 400 20"><line x1="100" y1="10" x2="300" y2="10" stroke="#999"/><rect x="188" y="2" width="24" height="16" fill="var(--band)"/><rect x="193" y="5" width="14" height="10" fill="none" stroke="#777"/></svg>
  <article class="abs card" style="left:99px">
    <div class="abs pic" role="img" aria-label="Blueprint rolls and drafting pen" style="background:linear-gradient(135deg,#d9e6f4,#6c9ccc 60%,#2d5f96)"></div>
    <h3>ENGINEERING</h3>
    <p>Lorem ipsum dolor sit amet, consectetuer adipiscing elit, sed diam nonummy nibh euismod tincidunt ut laoreet dolore magna aliquam erat volutpat. Ut wisi enim ad minim veniam</p>
    <div class="abs more">READ MORE</div>
  </article>
  <article class="abs card" style="left:617px">
    <div class="abs pic" role="img" aria-label="3D steel and floor plan detailing model" style="background:linear-gradient(135deg,#f1f1f1,#b8bcc2 55%,#6e8a8c)"></div>
    <h3>DETAILING</h3>
    <p>Lorem ipsum dolor sit amet, consectetuer adipiscing elit, sed diam nonummy nibh euismod tincidunt ut laoreet dolore magna aliquam erat volutpat. Ut wisi enim ad minim veniam</p>
    <div class="abs more">READ MORE</div>
  </article>
</section>

<section class="capabilities">
  <h2 class="abs title">Our <b>Capabilities</b></h2>
  <div class="abs cap-art" role="img" aria-label="Pencil sketch of cranes and buildings under construction"></div>
  <div class="abs cap-core"><div class="mark"></div><span>NORVALE DESIGN INC.</span></div>

  <div class="abs cap" style="left:208px;top:235px">
    <div class="ico" style="background:#1e4f8c"><svg width="40" height="48" viewBox="0 0 40 48"><circle cx="20" cy="18" r="14" fill="#fff"/><path d="M10 28l-4 18 8-4 4 6 2-16zM30 28l4 18-8-4-4 6-2-16z" fill="#fff"/><path d="M20 10l2.5 5 5.5.8-4 3.8 1 5.4-5-2.6-5 2.6 1-5.4-4-3.8 5.5-.8z" fill="#1e4f8c"/></svg></div>
    <div class="lbl">We Deliver<br>Quality</div>
  </div>
  <div class="abs dot" style="left:395px;top:281px"></div>

  <div class="abs cap" style="left:211px;top:388px">
    <div class="ico" style="background:#333"><svg width="44" height="44" viewBox="0 0 44 44"><circle cx="22" cy="22" r="18" fill="none" stroke="#fff" stroke-width="4"/><path d="M13 22l7 7 13-14" stroke="#fff" stroke-width="4" fill="none"/></svg></div>
    <div class="lbl">Always On<br>Time</div>
  </div>
  <div class="abs dot" style="left:393px;top:417px"></div>

  <div class="abs cap" style="left:801px;top:228px">
    <div class="ico" style="background:#333"><svg width="44" height="44" viewBox="0 0 44 44"><path d="M22 4l4 5 6-2 1 6 6 2-2 6 4 4-4 4 2 6-6 2-1 6-6-2-4 5-4-5-6 2-1-6-6-2 2-6-4-4 4-4-2-6 6-2 1-6 6 2z" fill="#fff"/><circle cx="22" cy="22" r="7" fill="#333"/></svg></div>
    <div class="lbl">We Are<br>Passionate</div>
  </div>
  <div class="abs dot" style="left:773px;top:264px"></div>

  <div class="abs cap" style="left:801px;top:384px">
    <div class="ico" style="background:#333"><svg width="48" height="40" viewBox="0 0 48 40"><circle cx="24" cy="12" r="7" fill="#fff"/><circle cx="11" cy="16" r="5" fill="#fff"/><circle cx="37" cy="16" r="5" fill="#fff"/><path d="M12 38a12 12 0 0 1 24 0zM1 38a10 10 0 0 1 13-9M47 38a10 10 0 0 0-13-9" fill="#fff"/></svg></div>
    <div class="lbl">Professional<br>Services</div>
  </div>
  <div class="abs dot" style="left:773px;top:423px"></div>
</section>

<section class="projects" role="img" aria-label="Downtown skyline at dusk reflected on wet pavement">
  <h2 class="abs title">Our Projects</h2>
  <svg class="abs divider" viewBox="0 0 400 20"><line x1="130" y1="10" x2="270" y2="10" stroke="#aaa"/></svg>
  <article class="abs proj" style="left:99px">
    <div class="abs pic" role="img" aria-label="Glass-fronted municipal building entrance" style="background:linear-gradient(180deg,#e4e7ea,#aab3bb 60%,#8a8f94)"></div>
    <div class="abs bar"><span>Municipal</span><div class="abs go"><svg width="16" height="12" viewBox="0 0 16 12"><path d="M2 1l5 5-5 5M9 1l5 5-5 5" stroke="#fff" stroke-width="2" fill="none"/></svg></div></div>
  </article>
  <article class="abs proj" style="left:441px">
    <div class="abs pic" role="img" aria-label="Modern commercial office building with blue glass" style="background:linear-gradient(180deg,#cfe1f1,#6f9fc4 55%,#c8cfd6)"></div>
    <div class="abs bar"><span>Commercial</span><div class="abs go"><svg width="16" height="12" viewBox="0 0 16 12"><path d="M2 1l5 5-5 5M9 1l5 5-5 5" stroke="#fff" stroke-width="2" fill="none"/></svg></div></div>
  </article>
  <article class="abs proj" style="left:783px">
    <div class="abs pic" role="img" aria-label="Large empty industrial warehouse interior" style="background:linear-gradient(180deg,#d8dde3,#9aa6b2 55%,#b7bcc1)"></div>
    <div class="abs bar"><span>Industrial</span><div class="abs go"><svg width="16" height="12" viewBox="0 0 16 12"><path d="M2 1l5 5-5 5M9 1l5 5-5 5" stroke="#fff" stroke-width="2" fill="none"/></svg></div></div>
  </article>
</section>
<div class="abs pager">
  <i><svg width="10" height="12" viewBox="0 0 10 12"><path d="M7 1L2 6l5 5" stroke="#333" stroke-width="2" fill="none"/></svg></i>
  <i><svg width="10" height="12" viewBox="0 0 10 12"><path d="M3 1l5 5-5 5" stroke="#333" stroke-width="2" fill="none"/></svg></i>
</div>

<section class="videos">
  <div class="video" role="img" aria-label="Video: cranes over high rise construction" style="background:linear-gradient(160deg,#c5c9cc,#6d747b)"><div class="play"><svg width="18" height="20" viewBox="0 0 18 20"><path d="M2 1l15 9-15 9z" fill="#555"/></svg></div></div>
  <div class="video" role="img" aria-label="Video: hard hat and plans on a desk" style="background:linear-gradient(160deg,#9fbbd4,#d6a43a 60%,#5b5f63)"><div class="play"><svg width="18" height="20" viewBox="0 0 18 20"><path d="M2 1l15 9-15 9z" fill="#555"/></svg></div></div>
  <div class="video" role="img" aria-label="Video: engineer holding rolled plans" style="background:linear-gradient(160deg,#e8e8e6,#3f73b3 60%,#d9c03b)"><div class="play"><svg width="18" height="20" viewBox="0 0 18 20"><path d="M2 1l15 9-15 9z" fill="#555"/></svg></div></div>
  <div class="video" role="img" aria-label="Video: 3D piping model on grey backdrop" style="background:linear-gradient(160deg,#9da3aa,#c0513d 55%,#4c5ea8)"><div class="play"><svg width="18" height="20" viewBox="0 0 18 20"><path d="M2 1l15 9-15 9z" fill="#555"/></svg></div></div>
  <div class="video" role="img" aria-label="Video: colour-coded ductwork model" style="background:linear-gradient(160deg,#1b2744,#3a58b8 50%,#b5a23a)"><div class="play"><svg width="18" height="20" viewBox="0 0 18 20"><path d="M2 1l15 9-15 9z" fill="#555"/></svg></div></div>
  <div class="video" role="img" aria-label="Video: plant room equipment model" style="background:linear-gradient(160deg,#3b3f45,#4cb6c0 55%,#a4a839)"><div class="play"><svg width="18" height="20" viewBox="0 0 18 20"><path d="M2 1l15 9-15 9z" fill="#555"/></svg></div></div>
</section>

<footer>
  <h4 style="left:103px">Contact Us</h4><div class="rule" style="left:103px;width:225px"></div>
  <div class="abs f-item" style="left:103px;top:100px"><div class="c"><svg width="10" height="14" viewBox="0 0 10 14"><path d="M5 0a5 5 0 0 1 5 5c0 4-5 9-5 9S0 9 0 5a5 5 0 0 1 5-5z" fill="#ccc"/><circle cx="5" cy="5" r="2" fill="#444"/></svg></div><div><b>NORVALE DESIGN INC</b>Lorem ipsum dolor sit amet,<br>consectetuer adipiscing elit</div></div>
  <div class="abs f-item" style="left:103px;top:168px;align-items:center"><div class="c"><svg width="12" height="12" viewBox="0 0 24 24"><path fill="#ccc" d="M6.6 10.8a15 15 0 0 0 6.6 6.6l2.2-2.2c.3-.3.7-.4 1-.2 1.1.4 2.3.6 3.6.6.6 0 1 .4 1 1V20c0 .6-.4 1-1 1A17 17 0 0 1 3 4c0-.6.4-1 1-1h3.5c.6 0 1 .4 1 1 0 1.3.2 2.5.6 3.6.1.3 0 .7-.2 1z"/></svg></div>555-018-2046</div>
  <div class="abs f-item" style="left:103px;top:214px;align-items:center"><div class="c"><svg width="12" height="9" viewBox="0 0 16 12"><rect width="16" height="12" fill="#ccc"/><path d="M1 1l7 6 7-6" stroke="#444" stroke-width="1.4" fill="none"/></svg></div>info@norvaledesign.com</div>

  <h4 style="left:408px">Newsletter Signup</h4><div class="rule" style="left:408px;width:250px"></div>
  <div class="abs news" style="left:408px;top:0;width:260px;height:200px">
    <p class="abs" style="left:4px;top:92px">Get the latest updates by entering your email address</p>
    <svg class="abs" style="left:150px;top:88px" width="64" height="50" viewBox="0 0 64 50"><path d="M2 20L62 2 40 48 30 30z" fill="#fff"/><path d="M30 30L62 2" stroke="#bbb" stroke-width="1.5"/></svg>
    <form style="top:188px"><div class="field">Enter your email here</div><div class="sub">Subscribe</div></form>
  </div>

  <h4 style="left:739px">Quick Links</h4><div class="rule" style="left:739px;width:120px"></div>
  <ul class="abs links" style="left:739px;top:84px"><li>Home</li><li>About Us</li><li>Our Service</li><li>Contact Us</li></ul>

  <h4 style="left:928px">Follow Us</h4>
  <div class="abs social" style="left:928px;top:76px"><i></i><i></i><i></i><i></i></div>
  <div class="abs f-brand" style="left:930px;top:150px"><div class="mark"></div><span>NORVALE DESIGN INC.</span></div>
</footer>
<div class="copy">Copyright © 2016. Norvale Design Inc. All Rights Reserved.</div>

</body>
</html>
```